Business Card for: Northbrook Financial Advisory Services Inc.

provide strategic financial advisory services to companies in the areas of corporate finance, mergers and acquisitions, executive coaching and strategic planning

Target Market(s)

Companies, banks, accountants, lawyers

Industry/Entity Type

High end business consulting in corporate finance, mergers and acquisitions, consulting

Contact Information for Business Card

Name of company, Name: xxxxxx xxxxxx , CEO, - phone number: 1-xxx-xxx-xxxx, - email address,

Requirements
Must have
• Must be professional and simple.
Nice to have
• simple, straight graphics, must give the impression that we are trustworthy, professional, competent
Should not have
• loud colors, loud design features

```html
<!DOCTYPE html>
<html lang="en">
<head>
<meta charset="utf-8">
<title>Northbrook Financial Advisory Services Inc. – Business Card</title>
<link rel="stylesheet" href="https://fonts.googleapis.com/css2?family=Open+Sans:wght@400;600&display=swap">
<style>
  :root {
    --backdrop: #b8e3f5;
    --cream: #e9ecdb;
    --navy: #221f57;
    --navy-deep: #1d1a4c;
    --pattern-blue: #34488f;
    --white: #ffffff;
  }
  * { margin: 0; padding: 0; box-sizing: border-box; }
  html, body {
    width: 1092px;
    height: 1200px;
    overflow: hidden;
    background: var(--backdrop);
    font-family: "Open Sans", sans-serif;
  }
  .card {
    position: absolute;
    left: 96px;
    width: 900px;
    height: 512px;
    background: var(--cream);
    overflow: hidden;
  }
  .card--front { top: 60px; }
  .card--back { top: 628px; }
  .card__shapes {
    position: absolute;
    inset: 0;
    width: 900px;
    height: 512px;
  }
  .brand {
    position: absolute;
    left: 0;
    right: 0;
    display: flex;
    align-items: center;
    justify-content: center;
    gap: 12px;
    color: var(--navy);
    font-weight: 600;
  }
  .brand__dot {
    width: 30px;
    height: 30px;
    border-radius: 50%;
    background: currentColor;
    flex: none;
  }
  .brand__name { display: flex; flex-direction: column; line-height: 1.05; }
  .brand__title { font-size: 32px; }
  .brand__subtitle { font-size: 15px; }
  .card--front .brand { top: 44px; }
  .card--back .brand { top: 222px; color: var(--white); }

  .person {
    position: absolute;
    left: 0;
    right: 0;
    top: 184px;
    text-align: center;
    color: var(--navy);
  }
  .person__name { font-size: 40px; font-weight: 400; line-height: 1.2; }
  .person__rule {
    width: 508px;
    height: 4px;
    margin: 4px auto 0;
    background: var(--navy);
  }
  .person__role { font-size: 24px; margin-top: 6px; }

  .contact {
    position: absolute;
    left: 250px;
    width: 408px;
    display: flex;
    align-items: center;
    gap: 10px;
  }
  .contact--phone { top: 320px; }
  .contact--email { top: 374px; }
  .contact__icon {
    width: 44px;
    height: 44px;
    border-radius: 8px;
    background: var(--navy);
    display: flex;
    align-items: center;
    justify-content: center;
    flex: none;
  }
  .contact__text {
    flex: 1;
    height: 34px;
    border-radius: 4px;
    background: var(--navy);
    color: var(--cream);
    font-size: 23px;
    line-height: 34px;
    padding-left: 28px;
  }
</style>
</head>
<body>

<section class="card card--front" aria-label="Business card front">
  <svg class="card__shapes" viewBox="0 0 900 512" aria-hidden="true">
    <path fill="var(--navy)" d="M0,118 Q0,140 18,144 Q36,148 36,170 V342 Q36,364 18,368 Q0,372 0,394 Z"/>
    <path fill="var(--navy)" d="M900,118 Q900,140 882,144 Q864,148 864,170 V342 Q864,364 882,368 Q900,372 900,394 Z"/>
  </svg>

  <div class="brand">
    <span class="brand__dot"></span>
    <span class="brand__name">
      <span class="brand__title">Northbrook</span>
      <span class="brand__subtitle">Financial Advisory Services Inc.</span>
    </span>
  </div>

  <div class="person">
    <p class="person__name">Your Name Here</p>
    <div class="person__rule"></div>
    <p class="person__role">CEO</p>
  </div>

  <div class="contact contact--phone">
    <span class="contact__icon">
      <svg width="26" height="26" viewBox="0 0 24 24" aria-hidden="true">
        <path fill="var(--cream)" d="M6.6 10.8a15.1 15.1 0 0 0 6.6 6.6l2.2-2.2a1 1 0 0 1 1-.25 11.4 11.4 0 0 0 3.6.57 1 1 0 0 1 1 1V20a1 1 0 0 1-1 1A17 17 0 0 1 3 4a1 1 0 0 1 1-1h3.5a1 1 0 0 1 1 1c0 1.25.2 2.45.57 3.57a1 1 0 0 1-.25 1z"/>
      </svg>
    </span>
    <span class="contact__text">+1-XXXX-XXXX</span>
  </div>

  <div class="contact contact--email">
    <span class="contact__icon">
      <svg width="28" height="22" viewBox="0 0 28 22" aria-hidden="true">
        <rect x="1" y="1" width="26" height="20" rx="2" fill="var(--cream)"/>
        <path d="M2 3 L14 12 L26 3" fill="none" stroke="var(--navy)" stroke-width="2.4"/>
      </svg>
    </span>
    <span class="contact__text">email@company.com</span>
  </div>
</section>

<section class="card card--back" aria-label="Business card back">
  <svg class="card__shapes" viewBox="0 0 900 512">
    <defs>
      <linearGradient id="backField" x1="0" y1="0" x2="1" y2="1">
        <stop offset="0" stop-color="var(--navy)"/>
        <stop offset="0.5" stop-color="var(--pattern-blue)" stop-opacity="0.9"/>
        <stop offset="1" stop-color="var(--navy-deep)"/>
      </linearGradient>
    </defs>
    <path role="img" aria-label="Navy field with a repeating pattern of diagonal blue wave lines"
          fill="var(--navy)"
          d="M36,0 H864 V96 Q864,118 882,122 Q900,126 900,148 V364 Q900,386 882,390 Q864,394 864,416 V512 H36 V416 Q36,394 18,390 Q0,386 0,364 V148 Q0,126 18,122 Q36,118 36,96 Z"/>
    <path fill="url(#backField)" opacity="0.25" aria-hidden="true"
          d="M36,0 H864 V96 Q864,118 882,122 Q900,126 900,148 V364 Q900,386 882,390 Q864,394 864,416 V512 H36 V416 Q36,394 18,390 Q0,386 0,364 V148 Q0,126 18,122 Q36,118 36,96 Z"/>
  </svg>

  <div class="brand">
    <span class="brand__dot"></span>
    <span class="brand__name">
      <span class="brand__title">Northbrook</span>
      <span class="brand__subtitle">Financial Advisory Services Inc.</span>
    </span>
  </div>
</section>

</body>
</html>
```